Small boutique multi-family apartment developer needs premium website design.

We are a growing real estate development company specializing in multi family apartment development. Our company Mireval Stone Development focuses on passive real estate investors looking to maximize their current real estate portfolio by allowing us to develop and reposition their current properties allowing them more cashflow while we are also able to take over the management of their asset in order to ensure optimal performance on a consistent basis.

```html
<!DOCTYPE html>
<html lang="en">
<head>
<meta charset="utf-8">
<title>Mireval Stone Development</title>
<link rel="stylesheet" href="https://fonts.googleapis.com/css2?family=Prata&family=Poppins:wght@300;400;500;600&display=swap">
<style>
:root{
  --navy:#3d4594;
  --navy-soft:#4a52a6;
  --navy-deep:#14163a;
  --gold:#e6b54b;
  --ink:#1d1d24;
  --text:#666870;
  --light:#f4f4f5;
  --white:#ffffff;
}
*{margin:0;padding:0;box-sizing:border-box}
html,body{width:1200px;height:4205px;overflow:hidden}
body{position:relative;background:var(--white);font-family:"Poppins",sans-serif;color:var(--ink)}
.abs{position:absolute}
.serif{font-family:"Prata",serif;font-weight:400}
.label{font-size:11px;color:var(--gold);text-transform:uppercase;letter-spacing:.5px}
.rule{width:44px;height:2px;background:var(--navy)}
.center{left:0;width:1200px;text-align:center}
.btn{background:var(--gold);color:var(--ink);font-size:10px;font-weight:500;letter-spacing:1px;text-transform:uppercase;display:flex;align-items:center;justify-content:center}
.photo{position:absolute}

/* top bar */
.topbar{top:0;left:0;width:1200px;height:30px;background:var(--navy);color:#fff;font-size:11px}
.topbar .info{left:140px;top:8px;display:flex;gap:18px;align-items:center}
.topbar .info span{display:flex;gap:6px;align-items:center}
.socials{display:flex;gap:8px}
.socials i{width:16px;height:16px;border:1px solid rgba(255,255,255,.8);border-radius:50%;display:block}
.socials i.on{background:var(--gold);border-color:var(--gold)}

/* hero */
.hero{top:30px;left:0;width:1200px;height:460px;background:linear-gradient(160deg,#6b5872 0%,#3a3440 30%,#26232a 60%,#1b1a1f 100%)}
.brand{display:flex;align-items:center;gap:10px;color:#fff}
.brand .mark{width:44px;height:44px;border:2px solid #fff}
.brand .name{font-family:"Prata",serif;font-size:15px;line-height:1.1}
.brand .tag{font-size:7px;letter-spacing:2px;border-top:1px solid #fff;margin-top:4px;padding-top:3px}
.nav{display:flex;gap:0;align-items:center;font-size:11px;color:#fff}
.nav a{padding:7px 14px;text-decoration:none;color:inherit}
.nav a.active{background:var(--gold);color:var(--ink)}
.hero h1{font-family:"Prata",serif;font-weight:400;font-size:34px;line-height:1.08;color:#fff}
.hero p{font-size:14px;color:#e6e6ec;line-height:1.4}
.outline-btn{border:1px solid rgba(255,255,255,.7);color:#fff;font-size:9px;letter-spacing:1px;display:flex;align-items:center;justify-content:center}

.card{position:absolute;box-shadow:0 8px 24px rgba(0,0,0,.12)}
.card h3{font-family:"Prata",serif;font-weight:400;font-size:17px;line-height:1.25}
.card p{font-size:9px;line-height:1.55}

/* why */
.why-col{position:absolute;width:240px;text-align:center}
.why-col h3{font-family:"Prata",serif;font-weight:400;font-size:17px;margin:18px 0 12px}
.why-col p{font-size:10.5px;line-height:2;color:var(--text)}

/* about */
.about{top:975px;left:0;width:1200px;height:529px;background:var(--light)}

/* services */
.services{top:1504px;left:0;width:1200px;height:588px;background:linear-gradient(100deg,#3a4190 0%,#4d55a3 50%,#3b428c 100%)}
.svc{position:absolute;top:206px;width:230px;height:292px;padding:40px 20px;color:#fff;border:1px solid rgba(255,255,255,.18);background:rgba(90,98,180,.45)}
.svc.featured{background:var(--gold);color:var(--ink);border-color:var(--gold)}
.svc h3{font-family:"Prata",serif;font-weight:400;font-size:17px;line-height:1.2;margin:14px 0 14px}
.svc p{font-size:10.5px;line-height:2}

/* testimonials */
.quote{font-family:"Prata",serif;font-size:34px;color:var(--ink)}
.testi-text{font-size:10.5px;line-height:2;color:var(--text);width:250px}
.testi-name{font-family:"Prata",serif;font-size:14px;margin-top:6px}
.stars{display:flex;gap:3px;margin-top:4px}

/* gallery */
.side-label{font-size:34px;letter-spacing:10px;color:#fff;writing-mode:vertical-rl;transform:rotate(180deg);font-weight:300}

/* contact */
.contact{top:3331px;left:0;width:1200px;height:529px;background:var(--navy)}
.contact-item{display:flex;gap:18px;color:#fff}
.contact-item .t{font-size:11px;margin-bottom:4px}
.contact-item .v{font-size:11px;line-height:1.6;color:#e2e3f0}
.form{top:3400px;left:629px;width:429px;height:504px;background:#fff;box-shadow:0 10px 30px rgba(0,0,0,.12)}
.field{position:absolute;left:30px;width:369px}
.field label{font-size:11px;font-weight:500;display:block;margin-bottom:6px}
.field .box{border:1px solid #e3e3e8;height:46px;font-size:11px;color:#999;padding:0 14px;display:flex;align-items:center;justify-content:space-between}

/* footer */
.footer{top:3860px;left:0;width:1200px;height:345px;background:var(--navy-deep);color:#fff}
.footer .links{display:flex;justify-content:center;font-size:11px}
.footer .links span{padding:0 32px;border-right:1px solid rgba(255,255,255,.25)}
.footer .links span:last-child{border:none}
</style>
</head>
<body>

<!-- top bar -->
<div class="abs topbar">
  <div class="abs info">
    <span><svg width="10" height="12" viewBox="0 0 10 12"><path d="M5 0a4 4 0 0 1 4 4c0 3-4 8-4 8S1 7 1 4a4 4 0 0 1 4-4z" fill="var(--gold)"/><circle cx="5" cy="4" r="1.5" fill="var(--navy)"/></svg>123 Lorem Ipsum Is Simply Dummy Text</span>
    <span><svg width="11" height="11" viewBox="0 0 24 24"><path d="M6 2l4 4-2 3a12 12 0 0 0 7 7l3-2 4 4-3 4C10 22 2 14 2 5z" fill="var(--gold)"/></svg>123 456 7890</span>
  </div>
  <div class="abs socials" style="left:962px;top:7px" aria-label="Social links"><i></i><i class="on"></i><i></i><i></i></div>
</div>

<!-- hero -->
<section class="abs hero">
  <div class="photo" role="img" aria-label="Modern multi-family apartment building at dusk" style="inset:0;background:linear-gradient(90deg,rgba(0,0,0,0) 40%,rgba(0,0,0,.35) 100%)"></div>
  <div class="abs brand" style="left:139px;top:20px">
    <div class="mark"></div>
    <div><div class="name">Mireval Stone Development</div><div class="tag">MULTI-FAMILY APARTMENT DEVELOPER</div></div>
  </div>
  <nav class="abs nav" style="left:609px;top:23px">
    <a class="active">HOME</a><a>ABOUT US</a><a>SERVICES</a><a>PORTFOLIO</a><a>CONTACT US</a>
  </nav>
  <h1 class="abs" style="left:677px;top:118px;width:420px">Transforming Properties, Maximizing Returns</h1>
  <p class="abs" style="left:677px;top:206px;width:400px">Partner With Mireval Stone Development To Optimize Your Real Estate Portfolio</p>
  <div class="abs outline-btn" style="left:677px;top:269px;width:98px;height:32px">CONTACT US</div>
  <svg class="abs" style="left:0;top:370px" width="1200" height="90" viewBox="0 0 1200 90">
    <polygon points="600,70 1200,22 1200,62" fill="var(--gold)"/>
    <polygon points="0,60 600,70 1200,62 1200,90 0,90" fill="#fff"/>
  </svg>
</section>

<div class="card" style="left:142px;top:335px;width:168px;height:199px;background:#fff;padding:28px 16px">
  <svg width="34" height="34" viewBox="0 0 34 34" fill="none" stroke="var(--gold)" stroke-width="1.5"><rect x="4" y="12" width="12" height="20"/><rect x="16" y="4" width="14" height="28"/><path d="M20 10h6M20 16h6M20 22h6M8 18h4M8 24h4"/></svg>
  <h3 style="margin:12px 0 10px">New Property Will Be Ready</h3>
  <p style="color:var(--ink)">Lorem Ipsum Is Simpl Dummy Text Of The Printi Typesetting Industry Centuries</p>
</div>
<div class="card" style="left:318px;top:335px;width:169px;height:199px;background:var(--navy);color:#fff;padding:44px 17px">
  <h3>Be The First</h3>
  <p style="margin:10px 0 14px">Lorem Ipsum Is Simpl Dummy Text Of The Printi Typesetting Industry Centuries.</p>
  <div class="btn" style="width:96px;height:30px;font-size:9px">CONTACT US</div>
</div>

<!-- why choose us -->
<h2 class="abs center serif" style="top:598px;font-size:33px">Why Choose Us</h2>
<p class="abs center" style="top:646px;font-size:11px;line-height:2;color:var(--text)">Lorem Ipsum Is Simply Dummy Text Of The Printing And Typesetting Industry. Lorem Ipsum Has Been The Industry's<br>Standard Dummy Text Ever Since The 1500s, When An Unknown Printer Took A Galley.</p>
<div class="abs rule" style="left:578px;top:697px"></div>

<div class="why-col" style="left:195px;top:732px">
  <svg width="56" height="52" viewBox="0 0 56 52" fill="none" stroke="var(--gold)" stroke-width="1.5"><rect x="6" y="14" width="18" height="36"/><rect x="24" y="4" width="22" height="46"/><rect x="46" y="24" width="6" height="26"/><path d="M10 20h10M10 28h10M10 36h10M29 10h12M29 18h12M29 26h12M29 34h12M2 50h52"/></svg>
  <h3>House For Everyone</h3>
  <p>Lorem Ipsum Is Simply Dummy Text Of The Printing And Typesetting Industry. Lorem Ipsum Has Been The Industry.</p>
</div>
<div class="why-col" style="left:479px;top:732px">
  <svg width="60" height="52" viewBox="0 0 60 52" fill="none" stroke="var(--gold)" stroke-width="1.5"><rect x="2" y="28" width="10" height="20"/><path d="M12 30l10-12 4-10c3 0 4 4 3 8l-2 6h10c3 0 4 3 2 5 2 2 1 5-2 6 1 2 0 5-3 5H12"/><rect x="34" y="2" width="22" height="30" rx="2"/><path d="M45 8v18M49 11h-6a3 3 0 0 0 0 6h4a3 3 0 0 1 0 6h-6"/></svg>
  <h3>Competitive Price</h3>
  <p>Lorem Ipsum Is Simply Dummy Text Of The Printing And Typesetting Industry. Lorem Ipsum Has Been The Industry.</p>
</div>
<div class="why-col" style="left:763px;top:732px">
  <svg width="56" height="52" viewBox="0 0 56 52" fill="none" stroke="var(--gold)" stroke-width="1.5"><circle cx="32" cy="18" r="14"/><circle cx="32" cy="18" r="9"/><path d="M32 12v6l4 3"/><path d="M4 38h10l8 4h10c3 0 3 4 0 4H20M14 46l10 4h14l14-10c2-2 0-5-3-4l-11 6"/></svg>
  <h3>Long-Term Investment</h3>
  <p>Lorem Ipsum Is Simply Dummy Text Of The Printing And Typesetting Industry. Lorem Ipsum Has Been The Industry.</p>
</div>

<!-- about -->
<section class="abs about">
  <div class="abs label" style="left:141px;top:124px">ABOUT US</div>
  <h2 class="abs serif" style="left:141px;top:144px;font-size:34px">Mireval Stone Development</h2>
  <p class="abs" style="left:141px;top:224px;width:430px;font-size:10.5px;line-height:2;color:var(--text)">Lorem Ipsum Is Simply Dummy Text Of The Printing And Typesetting Industry. Lorem Ipsum Has Been The Industry's Standard Dummy Text Ever Since The 1500s, When An Unknown Printer Took A Galley Of Type And Scrambled It To Make Typespecimen Book. It Has Survived Not Only Five Centuries, But Also The Leap Into Electronic Typesetting, Remaining Essentially Unchanged. It Was Popularised In The 1960s With The Release Of Letraset Sheets Containing Lorem Ipsum .</p>
  <div class="abs btn" style="left:141px;top:374px;width:115px;height:36px">CONTACT US</div>
  <div class="photo" role="img" aria-label="Modern apartment building with balconies and greenery" style="left:642px;top:135px;width:202px;height:304px;background:linear-gradient(180deg,#e8ecef 0%,#3a3c42 30%,#4d4a44 60%,#5e7a48 90%);box-shadow:0 8px 24px rgba(0,0,0,.15)"></div>
  <div class="photo" role="img" aria-label="Dark-clad apartment building with wood accents" style="left:856px;top:90px;width:204px;height:304px;background:linear-gradient(180deg,#eef1f3 0%,#2f3136 30%,#5a4e42 65%,#6a7d4e 92%);box-shadow:0 8px 24px rgba(0,0,0,.15)"></div>
</section>

<!-- services -->
<section class="abs services" role="img" aria-label="Apartment building facade under navy overlay">
  <div class="abs label center" style="top:90px">SERVICES</div>
  <h2 class="abs center serif" style="top:110px;font-size:33px;color:#fff">Our Services</h2>
  <div class="abs rule" style="left:578px;top:165px;background:#fff"></div>

  <div class="svc featured" style="left:142px">
    <svg width="48" height="50" viewBox="0 0 48 50" fill="none" stroke="var(--ink)" stroke-width="1.5"><circle cx="24" cy="34" r="12"/><path d="M24 28v12M27 30h-4a2 2 0 0 0 0 4h2a2 2 0 0 1 0 4h-4M24 22V10M24 12c-6-8-14-6-16-2 6 0 12 2 16 6M24 12c6-8 14-6 16-2-6 0-12 2-16 6"/></svg>
    <h3>Passive Real Estate Investing</h3>
    <p>Lorem Ipsum Is Simply Dummy Text Of The Printing And Typesetindustry. Lorem Ipsum Has Been Th Industry's Standard Dummy Text Ever.</p>
  </div>
  <div class="svc" style="left:371px">
    <svg width="48" height="50" viewBox="0 0 48 50" fill="none" stroke="var(--gold)" stroke-width="1.5"><rect x="18" y="6" width="20" height="40"/><rect x="6" y="24" width="12" height="22"/><path d="M22 12h12M22 18h12M22 24h12M22 30h12M22 36h12M2 46h42"/></svg>
    <h3>Property Development</h3>
    <p>Lorem Ipsum Is Simply Dummy Text Of The Printing And Typesetindustry. Lorem Ipsum Has Been Th Industry's Standard Dummy Text Ever.</p>
  </div>
  <div class="svc" style="left:601px">
    <svg width="48" height="50" viewBox="0 0 48 50" fill="none" stroke="var(--gold)" stroke-width="1.5"><circle cx="30" cy="14" r="8"/><circle cx="30" cy="14" r="3"/><rect x="6" y="22" width="14" height="24"/><path d="M10 28h6M10 34h6M10 40h6M24 46V30h16v16M2 46h44"/></svg>
    <h3>Property Management</h3>
    <p>Lorem Ipsum Is Simply Dummy Text Of The Printing And Typesetindustry. Lorem Ipsum Has Been Th Industry's Standard Dummy Text Ever.</p>
  </div>
  <div class="svc" style="left:830px">
    <svg width="48" height="50" viewBox="0 0 48 50" fill="none" stroke="var(--gold)" stroke-width="1.5"><path d="M18 14c-8 6-12 14-12 20a12 12 0 0 0 24 0c0-6-4-14-12-20z"/><path d="M14 6h8l-4 8zM18 24v16M21 27h-4a2 2 0 0 0 0 4h2a2 2 0 0 1 0 4h-4M28 44h16l-4-6"/></svg>
    <h3>Asset Optimization</h3>
    <p>Lorem Ipsum Is Simply Dummy Text Of The Printing And Typesetindustry. Lorem Ipsum Has Been Th Industry's Standard Dummy Text Ever.</p>
  </div>
</section>

<!-- testimonials -->
<div class="abs label center" style="top:2179px">TESTIMONIALS</div>
<h2 class="abs center serif" style="top:2198px;font-size:31px">What Our Client Says About Us</h2>
<div class="abs rule" style="left:578px;top:2255px"></div>

<div class="abs quote" style="left:150px;top:2272px">66</div>
<div class="abs" style="left:147px;top:2316px;width:155px;height:176px;background:var(--navy)"></div>
<div class="photo" role="img" aria-label="Client portrait" style="left:142px;top:2311px;width:155px;height:176px;background:linear-gradient(180deg,#d9dde2,#b7c4d2 60%,#7d95b3)"></div>
<div class="abs" style="left:331px;top:2312px">
  <p class="testi-text">Lorem Ipsum Is Simply Dummy Text Of Tprinting And Typesetting Industry. Lorem Ipsum Habeen The Industry's Standard Dummy Text Ever Since The 1500s, When An Unknown Printer Toogalley Of Type And Scrambled It To.</p>
  <div class="testi-name">Tomas Reyne</div>
  <div class="stars">
    <svg width="74" height="12" viewBox="0 0 74 12" fill="var(--gold)"><g id="s"><path d="M6 0l1.8 4 4.2.4-3.2 2.8 1 4.2L6 9.2 2.2 11.4l1-4.2L0 4.4 4.2 4z"/></g><use href="#s" x="15"/><use href="#s" x="30"/><use href="#s" x="45"/><use href="#s" x="60"/></svg>
  </div>
</div>
<div class="abs" style="left:600px;top:2305px;width:1px;height:180px;background:#e4e4e8"></div>

<div class="abs quote" style="left:635px;top:2272px">66</div>
<div class="abs" style="left:632px;top:2316px;width:155px;height:176px;background:var(--navy)"></div>
<div class="photo" role="img" aria-label="Client portrait" style="left:627px;top:2304px;width:155px;height:183px;background:linear-gradient(180deg,#e3e3e3,#d6cfc6 60%,#b6aca0)"></div>
<div class="abs" style="left:816px;top:2312px">
  <p class="testi-text">Lorem Ipsum Is Simply Dummy Text Of Tprinting And Typesetting Industry. Lorem Ipsum Habeen The Industry's Standard Dummy Text Ever Since The 1500s, When An Unknown Printer Toogalley Of Type And Scrambled It To.</p>
  <div class="testi-name">Tomas Reyne</div>
  <div class="stars"><svg width="74" height="12" viewBox="0 0 74 12" fill="var(--gold)"><use href="#s"/><use href="#s" x="15"/><use href="#s" x="30"/><use href="#s" x="45"/><use href="#s" x="60"/></svg></div>
</div>
<svg class="abs" style="left:582px;top:2510px" width="36" height="14" viewBox="0 0 36 14" fill="none" stroke="var(--ink)" stroke-width="1.5"><path d="M6 3l-4 4 4 4M30 3l4 4-4 4"/><path d="M18 0v14" stroke="#ccc"/></svg>

<!-- gallery -->
<div class="abs" style="top:2580px;left:0;width:1200px;height:727px;background:linear-gradient(180deg,#f7f7f9,#eceef4)" role="img" aria-label="Faded apartment buildings backdrop"></div>
<div class="abs label center" style="top:2620px">GALLERY</div>
<h2 class="abs center serif" style="top:2640px;font-size:31px">Our Work</h2>
<div class="abs rule" style="left:578px;top:2695px"></div>

<div class="photo" role="img" aria-label="Interior project photo" style="left:142px;top:2800px;width:158px;height:332px;background:linear-gradient(180deg,#3b3632,#5a4d40 50%,#2a2622)"></div>
<div class="abs side-label" style="left:188px;top:2880px">PREV</div>
<svg class="abs" style="left:152px;top:2958px" width="32" height="14" viewBox="0 0 32 14" fill="none" stroke="var(--gold)" stroke-width="1.5"><path d="M30 7H2M8 1L2 7l6 6"/></svg>

<div class="photo" role="img" aria-label="Modern building exterior" style="left:882px;top:2800px;width:176px;height:332px;background:linear-gradient(180deg,#37416a,#2a3150 40%,#8a8e98 100%)"></div>
<div class="abs side-label" style="left:970px;top:2880px">NEXT</div>
<svg class="abs" style="left:1014px;top:2958px" width="32" height="14" viewBox="0 0 32 14" fill="none" stroke="var(--gold)" stroke-width="1.5"><path d="M2 7h28M24 1l6 6-6 6"/></svg>

<div class="abs" style="left:367px;top:2742px;width:451px;height:449px;background:var(--navy)"></div>
<div class="photo" role="img" aria-label="Brick apartment complex with red balconies" style="left:300px;top:2752px;width:582px;height:424px;background:linear-gradient(180deg,#5a7ab8 0%,#9db4d8 25%,#b7805c 50%,#8a5a3e 70%,#2e2f2a 100%)"></div>
<div class="abs" style="left:300px;top:3020px;width:582px;height:156px;background:linear-gradient(180deg,rgba(0,0,0,0),rgba(0,0,0,.6))"></div>
<h3 class="abs serif" style="left:332px;top:3078px;font-size:19px;color:#fff">Contrary To Popular Belief</h3>
<p class="abs" style="left:332px;top:3110px;font-size:10.5px;line-height:2;color:#fff">Lorem Ipsum Is Simply Dummy Text Of The Printing And Typesetting Industry.<br>Lorem Ipsum Has Been The Industry's Standard Dummy .</p>

<!-- contact -->
<svg class="abs" style="left:0;top:3296px" width="1200" height="40" viewBox="0 0 1200 40">
  <polygon points="0,28 1200,10 1200,35 0,40" fill="var(--navy)"/>
  <polygon points="0,28 1200,4 1200,12 0,36" fill="var(--gold)"/>
</svg>
<section class="abs contact">
  <div class="abs label" style="left:141px;top:105px">CONTACT</div>
  <h2 class="abs serif" style="left:141px;top:125px;font-size:32px;color:#fff">Contact Details</h2>
  <p class="abs" style="left:141px;top:200px;width:420px;font-size:11px;line-height:2;color:#e2e3f0">Lorem Ipsum Odor Amet, Consectetuer Adipiscing Elit. Cubilia Montes Libero Sagittis Torquent Purus Platea.Facilisi Donec .</p>
  <div class="abs contact-item" style="left:150px;top:272px">
    <svg width="36" height="36" viewBox="0 0 36 36" fill="none" stroke="var(--gold)" stroke-width="1.5"><rect x="6" y="8" width="12" height="26"/><rect x="18" y="2" width="12" height="32"/><path d="M10 14h4M10 20h4M10 26h4M22 8h4M22 14h4M22 20h4M22 26h4"/></svg>
    <div><div class="t">Location</div><div class="v">123 Lorem Ipsum Odor Ametconsectetuer<br>Adipiscing Elit. Cubilia Montes.</div></div>
  </div>
  <div class="abs contact-item" style="left:150px;top:353px">
    <svg width="36" height="36" viewBox="0 0 36 36" fill="none" stroke="var(--gold)" stroke-width="1.5"><rect x="2" y="10" width="32" height="22"/><path d="M2 10l16 12 16-12"/></svg>
    <div><div class="t">Email Address</div><div class="v">hello@mirevalstone.com</div></div>
  </div>
  <div class="abs contact-item" style="left:150px;top:425px">
    <svg width="36" height="36" viewBox="0 0 24 24" fill="none" stroke="var(--gold)" stroke-width="1.2"><path d="M6 2l4 4-2 3a12 12 0 0 0 7 7l3-2 4 4-3 4C10 22 2 14 2 5z"/><path d="M14 2a8 8 0 0 1 8 8M14 6a4 4 0 0 1 4 4"/></svg>
    <div><div class="t">Phone Number</div><div class="v" style="font-size:14px;color:#fff">(123) 456 7890</div></div>
  </div>
</section>

<div class="abs form">
  <h2 class="abs serif" style="left:0;width:429px;top:34px;text-align:center;font-size:30px">Quick Inquiry</h2>
  <div class="field" style="top:90px"><label>Full Name</label><div class="box">Enter Your Name<svg width="12" height="12" viewBox="0 0 12 12" fill="#aaa"><circle cx="6" cy="3.5" r="2.5"/><path d="M1 12a5 5 0 0 1 10 0z"/></svg></div></div>
  <div class="field" style="top:154px"><label>Phone No</label><div class="box">123 456 7890<svg width="12" height="12" viewBox="0 0 24 24" fill="#aaa"><path d="M6 2l4 4-2 3a12 12 0 0 0 7 7l3-2 4 4-3 4C10 22 2 14 2 5z"/></svg></div></div>
  <div class="field" style="top:220px"><label>Email Address</label><div class="box">info@mirevalstone.com<svg width="13" height="10" viewBox="0 0 13 10" fill="#aaa"><rect width="13" height="10"/><path d="M0 0l6.5 5L13 0" stroke="#fff" fill="none"/></svg></div></div>
  <div class="field" style="top:288px"><label>Message</label><div class="box" style="height:98px;align-items:flex-start;padding-top:14px">Type Your Message Here!<svg width="12" height="12" viewBox="0 0 12 12" fill="#aaa"><circle cx="6" cy="6" r="6"/></svg></div></div>
  <div class="abs btn" style="left:30px;top:414px;width:369px;height:42px">SUBMIT NOW</div>
</div>

<!-- footer -->
<footer class="abs footer">
  <div class="abs brand" style="left:444px;top:88px">
    <div class="mark" style="width:58px;height:58px"></div>
    <div><div class="name" style="font-size:19px">Mireval Stone Development</div><div class="tag" style="font-size:8.5px">MULTI-FAMILY APARTMENT DEVELOPER</div></div>
  </div>
  <div class="abs links" style="left:0;width:1200px;top:176px">
    <span>HOME</span><span>ABOUT US</span><span>SERVICES</span><span>PORTFOLIO</span><span>CONTACT US</span>
  </div>
  <div class="abs socials" style="left:538px;top:222px;gap:10px" aria-label="Social links">
    <i style="width:24px;height:24px"></i><i class="on" style="width:24px;height:24px"></i><i style="width:24px;height:24px"></i><i style="width:24px;height:24px"></i>
  </div>
  <div class="abs" style="left:141px;top:288px;width:918px;height:1px;background:rgba(255,255,255,.2)"></div>
  <p class="abs center" style="top:305px;font-size:11px;color:#d8d9e6">© 2024 Mireval Stone Development. All Rights Reserved.</p>
</footer>

</body>
</html>
```